Business Cards/ Stationery for Dental Office
Willow Gate Dental
Business Cards/ Stationery for Dental Office - Health
Creative Brief
Simple
Celia R. Marlow, DDS
2715 Pelton Ridge Franklin, Tn 37069
willowgatedental@mailvane.com
www.willowgatedental.com
Please also add a facebook icon. Link is www.facebook/willowgatedental Also, for the business cards I would like one business card with logo on one side and all pertinent info on the other side. Then another business card (for older people who might actually want an appointment card) that on the back side says Appointment at the top. Then says Name:, Date:, Time:

```html
<!DOCTYPE html>
<html lang="en">
<head>
<meta charset="utf-8">
<title>Willow Gate Dental – Business Cards</title>
<link rel="stylesheet" href="https://fonts.googleapis.com/css2?family=Questrial&family=Tinos:ital,wght@0,400;1,400;1,700&display=swap">
<style>
  :root {
    --backdrop: #e4e4e2;
    --card: #ffffff;
    --ink: #2e2e2e;
    --grey: #6d6d6d;
    --rule: #8a8a8a;
    --faint: #e6e6e6;
    --accent: #e8c92a;
    --tab: #8f8f8f;
  }
  * { box-sizing: border-box; margin: 0; padding: 0; }
  html, body { width: 1200px; height: 901px; overflow: hidden; background: var(--backdrop); }
  .stage { position: relative; width: 1200px; height: 901px; }

  .card {
    position: absolute;
    width: 560px; height: 320px;
    background: var(--card);
    border-radius: 14px;
    box-shadow: 0 6px 18px rgba(0,0,0,.18);
    overflow: hidden;
  }

  /* Appointment side */
  .appointment-card { left: 90px; top: 90px; font-family: "Tinos", serif; color: var(--ink); }
  .appointment-card .watermark {
    position: absolute; left: 0; right: 0; top: 118px;
    text-align: center; font-family: "Questrial", sans-serif;
    font-size: 46px; letter-spacing: 2px; color: var(--faint);
  }
  .appointment-card .title {
    position: absolute; left: 30px; top: 40px;
    font-style: italic; font-weight: 700; font-size: 15px;
    border-bottom: 1px solid var(--ink);
  }
  .field { position: absolute; left: 30px; right: 30px; display: flex; align-items: flex-end; gap: 6px; font-size: 14px; }
  .field .fill { flex: 1; border-bottom: 1px solid var(--rule); height: 14px; }
  .field-day { top: 80px; } .field-time { top: 138px; } .field-with { top: 196px; }
  .notice {
    position: absolute; left: 30px; right: 30px; top: 250px;
    font-style: italic; font-size: 12.5px; text-decoration: underline;
  }

  /* Logo + contact side */
  .contact-card { left: 550px; top: 470px; font-family: "Questrial", sans-serif; }
  .contact-card .tab { position: absolute; top: 70px; width: 8px; height: 180px; background: var(--tab); border-radius: 4px; }
  .tab-left { left: 0; } .tab-right { right: 0; }
  .brand { position: absolute; left: 40px; top: 110px; width: 240px; display: flex; align-items: center; gap: 10px; }
  .brand-dot { width: 16px; height: 16px; border-radius: 50%; background: var(--grey); flex: none; }
  .brand-name { font-size: 26px; color: var(--grey); line-height: 1.15; }
  .divider { position: absolute; left: 295px; top: 70px; width: 1px; height: 180px; background: var(--faint); }
  .details { position: absolute; left: 315px; top: 92px; width: 230px; color: var(--grey); font-size: 12.5px; }
  .details .name { color: var(--accent); font-size: 15px; margin-bottom: 10px; }
  .details .address { line-height: 1.35; margin-bottom: 16px; }
  .contact-list { list-style: none; }
  .contact-list li { display: flex; align-items: center; gap: 8px; line-height: 1.5; }
  .contact-list svg { width: 12px; height: 12px; fill: var(--grey); flex: none; }
</style>
</head>
<body>
<main class="stage">

  <section class="card appointment-card" aria-label="Appointment card">
    <div class="watermark" aria-hidden="true">WILLOW GATE DENTAL</div>
    <h2 class="title">Your Next Appointment</h2>
    <div class="field field-day"><span>Appointment Day</span><span class="fill"></span></div>
    <div class="field field-time"><span>Appointment Time</span><span class="fill"></span><span>A.M.</span><span class="fill"></span><span>P.M.</span></div>
    <div class="field field-with"><span>Appointment With</span><span class="fill"></span></div>
    <p class="notice">We kindly ask for a 24hr notice for cancellations of appointments otherwise a charge may be incurred.</p>
  </section>

  <section class="card contact-card" aria-label="Business card">
    <span class="tab tab-left"></span><span class="tab tab-right"></span>
    <div class="brand"><span class="brand-dot"></span><span class="brand-name">Willow Gate Dental</span></div>
    <span class="divider"></span>
    <div class="details">
      <p class="name">Celia R. Marlow, DDS</p>
      <p class="address">2715 Pelton Ridge<br>Franklin, Tn 37069</p>
      <ul class="contact-list">
        <li><svg viewBox="0 0 12 12"><path d="M2 1h2.5l1 3-1.5 1a6 6 0 0 0 3 3l1-1.5 3 1V10a1 1 0 0 1-1 1A9 9 0 0 1 1 2a1 1 0 0 1 1-1z"/></svg>615-555-0142</li>
        <li><svg viewBox="0 0 12 12"><path d="M3 1h5v3H3zM1 5h10v5H9V8H3v2H1zM4 9h4v2H4z"/></svg>615-555-0187</li>
        <li><svg viewBox="0 0 12 12"><path d="M1 2.5h10v7H1zM1.8 3.2 6 6.5l4.2-3.3v.9L6 7.4 1.8 4.1z" fill-rule="evenodd"/></svg>willowgatedental@mailvane.com</li>
        <li><svg viewBox="0 0 12 12"><circle cx="6" cy="6" r="5"/><path d="M1 6h10M6 1c2 2.5 2 7.5 0 10M6 1c-2 2.5-2 7.5 0 10" stroke="#fff" stroke-width=".8" fill="none"/></svg>www.willowgatedental.com</li>
      </ul>
    </div>
  </section>

</main>
</body>
</html>
```